Brackenford Hearing Clinic Business Card Design Project

We need a new business card design. We changed our logo recently and need to update our cards. We are a small hearing clinic with a 3 locations in BC. We help people with hearing loss by fitting them with hearing instruments that are appropriate for them and help them overcome the challenges that hearing loss causes. The symbol part of our logo represents the three important components of successful outcome. The three are: 1-acceptance of the change in hearing, 2-a hearing care provider that cares and is knowledgeable and experienced, 3-a quality hearing instrument. I would like to have a clean design that shows quality commitment to a successful end result of treatment. Here is our website for more information. www.earlumo.ca

Target Market(s)

Senior population - mostly 50+

Industry/Entity Type

Clinic

Requirements
Must have
• Logo
Name - Devon Pallister
Title - Hearing Instrument Practitioner (can be very small)
Phone: 250 637-4819
Address: 415-B 22nd Street, Ashgrove Bay, BC V2X 2K7
Email: devon@earlumo.ca
website address: www.earlumo.ca
Nice to have
• Could be both sided and have a photo on the card.

```html
<!DOCTYPE html>
<html lang="en">
<head>
<meta charset="utf-8">
<title>Brackenford Hearing Clinic – Business Card</title>
<link rel="stylesheet" href="https://fonts.googleapis.com/css2?family=Varela+Round&display=swap">
<style>
  :root {
    --page-bg: #ecebe8;
    --card-white: #ffffff;
    --sky-light: #eef5fd;
    --sky-deep: #6fb0ee;
    --brand-blue: #1f86e8;
    --ink: #1e1e1e;
    --ink-soft: #444444;
    --icon-grey: #555555;
    --photo-warm: #b44d22;
    --photo-deep: #3b2a8c;
    --shadow: rgba(0, 0, 0, 0.18);
  }
  * { box-sizing: border-box; margin: 0; padding: 0; }
  html, body { width: 1200px; height: 1000px; overflow: hidden; }
  body {
    background: var(--page-bg);
    font-family: "Varela Round", sans-serif;
    font-weight: 400;
    color: var(--ink);
    display: flex;
    flex-direction: column;
    align-items: center;
    justify-content: center;
    gap: 60px;
  }
  .card {
    width: 700px;
    height: 400px;
    border-radius: 4px;
    box-shadow: 0 10px 28px var(--shadow);
    position: relative;
    overflow: hidden;
  }

  /* Front side */
  .card-front {
    background: linear-gradient(160deg, var(--card-white) 0%, var(--sky-light) 35%, var(--sky-deep) 100%);
  }
  .brand {
    position: absolute;
    left: 90px;
    top: 100px;
    display: flex;
    align-items: center;
    gap: 22px;
  }
  .brand-dot {
    width: 54px;
    height: 54px;
    border-radius: 50%;
    background: var(--brand-blue);
    flex: none;
  }
  .brand-name {
    font-size: 46px;
    font-weight: 400;
    line-height: 1.1;
    color: var(--brand-blue);
  }
  .contact-row {
    position: absolute;
    left: 48px;
    right: 40px;
    bottom: 58px;
    display: flex;
    justify-content: space-between;
    font-size: 17px;
    color: var(--ink);
  }
  .contact-item { display: flex; align-items: center; gap: 7px; white-space: nowrap; }
  .contact-item svg { width: 16px; height: 16px; flex: none; }

  /* Back side */
  .card-back {
    background: var(--card-white);
    display: flex;
  }
  .team-photo {
    width: 300px;
    height: 100%;
    background: linear-gradient(135deg, var(--photo-deep) 0%, var(--photo-deep) 35%, var(--photo-warm) 70%, #d8792f 100%);
    flex: none;
  }
  .spectrum-rule {
    width: 5px;
    height: 100%;
    background: linear-gradient(180deg, #e53935, #fb8c00, #fdd835, #43a047, #1e88e5, #8e24aa);
    flex: none;
  }
  .practitioner {
    flex: 1;
    padding: 80px 40px 0 44px;
    position: relative;
  }
  .practitioner-name {
    font-size: 40px;
    font-weight: 400;
    color: var(--ink);
    white-space: nowrap;
  }
  .practitioner-title {
    font-size: 15px;
    color: var(--ink-soft);
    margin-top: 8px;
  }
  .address {
    position: absolute;
    left: 44px;
    bottom: 70px;
    display: flex;
    gap: 10px;
    font-size: 20px;
    line-height: 1.35;
    color: var(--ink);
  }
  .address p { white-space: nowrap; }
  .address svg { width: 18px; height: 22px; flex: none; margin-top: 3px; }
</style>
</head>
<body>

  <section class="card card-front" aria-label="Business card front">
    <div class="brand">
      <span class="brand-dot"></span>
      <span class="brand-name">Brackenford<br>Hearing Clinic</span>
    </div>
    <div class="contact-row">
      <span class="contact-item">
        <svg viewBox="0 0 16 16" aria-hidden="true"><path d="M2 8 L8 2.5 L14 8 M4 7 V14 H12 V7" fill="none" stroke="var(--icon-grey)" stroke-width="1.5" stroke-linejoin="round"/></svg>
        www.earlumo.ca
      </span>
      <span class="contact-item">
        <svg viewBox="0 0 16 16" aria-hidden="true"><circle cx="8" cy="8" r="3" fill="none" stroke="var(--icon-grey)" stroke-width="1.5"/><path d="M11 8 V9.5 A2 2 0 0 0 15 9 V8 A7 7 0 1 0 11.5 14" fill="none" stroke="var(--icon-grey)" stroke-width="1.5"/></svg>
        devon@earlumo.ca
      </span>
      <span class="contact-item">
        <svg viewBox="0 0 16 16" aria-hidden="true"><path d="M4 1.5 L6.5 4.5 L5 6.5 Q6.5 9.5 9.5 11 L11.5 9.5 L14.5 12 L12.5 14.5 Q5 13 1.5 3.5 Z" fill="var(--icon-grey)"/></svg>
        250 637-4819
      </span>
    </div>
  </section>

  <section class="card card-back" aria-label="Business card back">
    <div class="team-photo" role="img" aria-label="Photo of the clinic's practitioners standing together in the clinic"></div>
    <div class="spectrum-rule"></div>
    <div class="practitioner">
      <h1 class="practitioner-name">Devon Pallister</h1>
      <p class="practitioner-title">Hearing Instrument Practitioner</p>
      <div class="address">
        <svg viewBox="0 0 18 22" aria-hidden="true"><path d="M9 21 C4 14 2 11 2 8 A7 7 0 0 1 16 8 C16 11 14 14 9 21 Z" fill="none" stroke="var(--icon-grey)" stroke-width="1.6"/><circle cx="9" cy="8" r="2.5" fill="var(--icon-grey)"/></svg>
        <p>415-B 22nd Street,<br>Ashgrove Bay, BC V2X 2K7</p>
      </div>
    </div>
  </section>

</body>
</html>
```